need a Facebook marketing ad for Kordell Welding

www.kordellwelding.com is our website to look at, I need someone to design a 15-30 second ad video/sideshow for a general welding and fabrication shop, tig welding, trailer repair, build staircases, pipe welding. I don't have the media or the artistic abilities to do it. Attached is what I have, fill in the blanks and add to it.

would like to get
1-2 video ads
1-2 graphic ads
1-2 different yard signs

```html
<!DOCTYPE html>
<html lang="en">
<head>
<meta charset="utf-8">
<title>Kordell Welding – Services</title>
<link rel="stylesheet" href="https://fonts.googleapis.com/css2?family=Michroma&family=Russo+One&display=swap">
<style>
  :root {
    --ink: #0b0b0c;
    --panel: #151517;
    --red: #e3262b;
    --red-deep: #a50f14;
    --red-bright: #ff3b3b;
    --silver: #d9d9d9;
    --silver-dark: #8d8d8d;
    --white: #ffffff;
  }
  * { margin: 0; padding: 0; box-sizing: border-box; }
  html, body { width: 1200px; height: 1200px; overflow: hidden; background: var(--ink); }
  .ad {
    position: relative;
    width: 1200px;
    height: 1200px;
    overflow: hidden;
    background: radial-gradient(ellipse at 50% 45%, #1e1e21 0%, var(--panel) 45%, var(--ink) 100%);
    font-family: "Michroma", "Arial Black", sans-serif;
    color: var(--white);
  }
  .frame-shapes { position: absolute; inset: 0; }

  .title {
    position: absolute;
    left: 0; right: 0;
    top: 166px;
    text-align: center;
    font-family: "Russo One", sans-serif;
    font-size: 48px;
    font-style: italic;
    letter-spacing: 1px;
    color: var(--silver);
    padding-left: 16px;
  }

  .service {
    position: absolute;
    display: flex;
    align-items: center;
    gap: 26px;
  }
  .service-label {
    font-size: 26px;
    line-height: 35px;
    letter-spacing: 1px;
    text-transform: uppercase;
    color: var(--white);
  }
  .service-icon {
    flex: none;
    border-radius: 14px;
    background: linear-gradient(160deg, var(--red-bright), var(--red-deep));
  }
  .svc-welding { left: 116px; top: 412px; }
  .svc-welding .service-icon { width: 108px; height: 118px; }
  .svc-plasma { left: 706px; top: 384px; }
  .svc-plasma .service-icon { width: 92px; height: 128px; }
  .svc-cutting { left: 120px; top: 604px; }
  .svc-cutting .service-icon { width: 104px; height: 104px; border-radius: 50%; }
  .svc-testing { left: 700px; top: 578px; }
  .svc-testing .service-icon { width: 116px; height: 112px; }
  .svc-inspection { left: 334px; top: 744px; }

  .brand {
    position: absolute;
    left: 0; top: 1060px;
    width: 434px;
    text-align: center;
    font-family: "Russo One", sans-serif;
    font-size: 38px;
    line-height: 44px;
    color: var(--white);
  }

  .cta {
    position: absolute;
    left: 618px;
    top: 1090px;
    font-family: "Russo One", sans-serif;
    color: var(--white);
  }
  .cta-label {
    display: block;
    margin-left: 54px;
    font-size: 34px;
    font-style: italic;
    letter-spacing: 1px;
  }
  .cta-phone {
    display: flex;
    align-items: center;
    gap: 12px;
    font-size: 46px;
    letter-spacing: 2px;
    margin-top: 2px;
  }
</style>
</head>
<body>
<main class="ad">
  <svg class="frame-shapes" width="1200" height="1200" viewBox="0 0 1200 1200" aria-hidden="true">
    <defs>
      <linearGradient id="redCorner" x1="0" y1="0" x2="1" y2="1">
        <stop offset="0" stop-color="#ff4a4a"/>
        <stop offset="1" stop-color="#b0121a"/>
      </linearGradient>
      <linearGradient id="silverBand" x1="0" y1="0" x2="1" y2="1">
        <stop offset="0" stop-color="#f2f2f2"/>
        <stop offset="1" stop-color="#7a7a7a"/>
      </linearGradient>
      <linearGradient id="redBand" x1="0" y1="0" x2="1" y2="0">
        <stop offset="0" stop-color="#b5121a"/>
        <stop offset="0.45" stop-color="#ff3a3a"/>
        <stop offset="1" stop-color="#b0121a"/>
      </linearGradient>
      <linearGradient id="titleRule" x1="0" y1="0" x2="1" y2="0">
        <stop offset="0" stop-color="#e3262b" stop-opacity="0"/>
        <stop offset="0.7" stop-color="#e3262b"/>
        <stop offset="1" stop-color="#ff3b3b"/>
      </linearGradient>
    </defs>
    <!-- top-left corner -->
    <polygon points="0,0 318,0 50,278 0,278" fill="url(#silverBand)"/>
    <polygon points="0,0 272,0 0,272" fill="url(#redCorner)"/>
    <!-- title rule -->
    <rect x="364" y="226" width="560" height="6" rx="3" fill="url(#titleRule)"/>
    <circle cx="866" cy="229" r="9" fill="#ff4a4a"/>
    <!-- right silver wedge -->
    <polygon points="1200,752 1200,1052 1060,1052" fill="url(#silverBand)"/>
    <!-- bottom red band -->
    <rect x="420" y="1050" width="780" height="150" fill="url(#redBand)"/>
    <rect x="420" y="1050" width="780" height="6" fill="#7c0a0f"/>
    <!-- bottom-left brand disc -->
    <circle cx="214" cy="1124" r="250" fill="url(#silverBand)"/>
    <circle cx="206" cy="1132" r="242" fill="#050505"/>
  </svg>

  <h1 class="title">SERVICES</h1>

  <div class="service svc-welding">
    <div class="service-icon" role="img" aria-label="Welding helmet and torch icon"></div>
    <p class="service-label">Welding<br>&amp; Fabrication</p>
  </div>

  <div class="service svc-plasma">
    <div class="service-icon" role="img" aria-label="Plasma cutter head with sparks icon"></div>
    <p class="service-label">CNC Plasma<br>or Torch</p>
  </div>

  <div class="service svc-cutting">
    <div class="service-icon" role="img" aria-label="Cutting disc icon"></div>
    <p class="service-label">Steel Cutting</p>
  </div>

  <div class="service svc-testing">
    <div class="service-icon" role="img" aria-label="Welder in helmet icon"></div>
    <p class="service-label">Welder<br>Testing</p>
  </div>

  <div class="service svc-inspection">
    <svg width="112" height="118" viewBox="0 0 112 118" aria-label="Magnifying glass icon" role="img">
      <circle cx="62" cy="50" r="38" fill="none" stroke="#e3262b" stroke-width="14"/>
      <line x1="34" y1="80" x2="10" y2="106" stroke="#d9d9d9" stroke-width="14" stroke-linecap="round"/>
    </svg>
    <p class="service-label">Inspection and<br>Consulting</p>
  </div>

  <p class="brand">Kordell<br>Welding</p>

  <div class="cta">
    <span class="cta-label">CALL NOW</span>
    <span class="cta-phone">
      <svg width="46" height="46" viewBox="0 0 24 24" aria-hidden="true">
        <path fill="#ffffff" d="M6.6 10.8a15.1 15.1 0 0 0 6.6 6.6l2.2-2.2a1 1 0 0 1 1-.25 11.4 11.4 0 0 0 3.6.57 1 1 0 0 1 1 1V20a1 1 0 0 1-1 1A17 17 0 0 1 3 4a1 1 0 0 1 1-1h3.5a1 1 0 0 1 1 1c0 1.25.2 2.45.57 3.57a1 1 0 0 1-.25 1z"/>
      </svg>
      931-555-0147
    </span>
  </div>
</main>
</body>
</html>
```